Business Card Design Project

We need a redesign of our business card.
We are a Consulting Property Developer called The Kestrel Group
Updates

Thank you all for submissions. Just waiting on managment to decide.

Thank you,

Dorinda

Industry/Entity Type

Business

Requirements
Must have
• we like having the KG a focus in the back ground or on the side
Kestrel is our company colour

the wording - property development
and - premium accommodation

our website www.kestrelgroup-example.com.au

persons name
title

p: 1300 482917 f: 1300 482915 m: 0417593824
PO Box 5817, Brindlevale Qld 4178
e: admin@kestrelgroup-example.com.au

```html
<!DOCTYPE html>
<html lang="en">
<head>
<meta charset="utf-8">
<title>The Kestrel Group – Business Card</title>
<link href="https://fonts.googleapis.com/css2?family=Open+Sans:ital,wght@0,300;0,400;1,400&display=swap" rel="stylesheet">
<style>
  :root {
    --backdrop: #3b3b3d;
    --kestrel: #861c2c;
    --kestrel-text: #b0223a;
    --card-dark: #1c1c1e;
    --rule-grey: #4a4b4d;
    --silver: #c8c8ca;
    --silver-soft: #a9a9ab;
  }
  * { box-sizing: border-box; margin: 0; padding: 0; }
  html, body {
    width: 1200px; height: 534px; overflow: hidden;
    background: var(--backdrop);
    font-family: "Open Sans", Arial, sans-serif;
  }
  .canvas { position: relative; width: 1200px; height: 534px; }

  .card {
    position: absolute; top: 119px; width: 517px; height: 295px;
    border-radius: 14px; overflow: hidden;
    background: var(--card-dark);
  }
  .card--front { left: 62px; }
  .card--back { left: 622px; }

  .card__band {
    position: absolute; left: 0; width: 100%; height: 46px;
    background: var(--kestrel);
  }
  .card__band--top { top: 0; }
  .card__band--bottom { bottom: 0; }
  .card__rule {
    position: absolute; left: 0; width: 100%; height: 3px;
    background: var(--rule-grey);
  }
  .card__rule--top { top: 52px; }
  .card__rule--bottom { bottom: 52px; }

  /* Front */
  .brand {
    position: absolute; left: 20px; top: 112px; width: 456px;
    display: flex; align-items: flex-end; gap: 12px;
    color: var(--silver); font-weight: 300;
  }
  .brand__initials { font-size: 40px; line-height: 1; letter-spacing: 1px; }
  .brand__divider { width: 1px; height: 54px; background: var(--silver); transform: skewX(-8deg); }
  .brand__name { font-size: 36px; line-height: 1; }
  .brand__underline {
    position: absolute; left: 20px; top: 160px; width: 444px; height: 1px;
    background: var(--silver-soft);
  }
  .tagline {
    position: absolute; left: 0; width: 100%; top: 203px;
    text-align: center; font-size: 12.5px; color: var(--silver-soft);
  }

  /* Back */
  .monogram {
    position: absolute; left: 30px; top: 82px;
    font-size: 84px; font-weight: 300; line-height: 1; color: var(--silver);
  }
  .monogram__rule {
    position: absolute; left: 14px; top: 178px; width: 241px; height: 1px;
    background: var(--silver-soft);
  }
  .contact__divider {
    position: absolute; left: 255px; top: 86px; width: 1px; height: 92px;
    background: var(--silver-soft); transform: skewX(-8deg);
  }
  .contact {
    position: absolute; left: 270px; top: 86px;
    font-style: italic; font-size: 11.5px; line-height: 13.3px; color: var(--silver);
  }
  .contact__name { color: var(--kestrel-text); font-weight: 400; font-size: 12px; text-transform: uppercase; letter-spacing: .3px; }
  .contact__title { margin-left: 2px; }
  .contact__address { margin: 9px 0 8px 3px; }
  .contact__list { list-style: none; margin-left: 3px; }
  .contact__list li:nth-child(2) { margin-left: 4px; }
  .contact__list li:nth-child(4) { margin-left: 0; }
  .contact__list li:nth-child(5) { margin-left: -4px; }
  .contact__key { color: var(--kestrel-text); }
</style>
</head>
<body>
<main class="canvas">
  <section class="card card--front" aria-label="Card front">
    <div class="card__band card__band--top"></div>
    <div class="card__rule card__rule--top"></div>
    <div class="brand">
      <span class="brand__initials">KG</span>
      <span class="brand__divider"></span>
      <span class="brand__name">The Kestrel Group</span>
    </div>
    <div class="brand__underline"></div>
    <p class="tagline">Property Development&nbsp; | &nbsp;Premium Accommodation</p>
    <div class="card__rule card__rule--bottom"></div>
    <div class="card__band card__band--bottom"></div>
  </section>

  <section class="card card--back" aria-label="Card back">
    <div class="card__band card__band--top"></div>
    <div class="card__rule card__rule--top"></div>
    <div class="monogram">KG</div>
    <div class="monogram__rule"></div>
    <div class="contact__divider"></div>
    <div class="contact">
      <p class="contact__name">John Doe</p>
      <p class="contact__title">Title</p>
      <p class="contact__address">PO Box 5817, Brindlevale Qld 4178</p>
      <ul class="contact__list">
        <li><span class="contact__key">p:</span> 1300 482917</li>
        <li><span class="contact__key">f:</span> 1300 482915</li>
        <li><span class="contact__key">m:</span> 0417593824</li>
        <li><span class="contact__key">e:</span> admin@kestrelgroup-example.com.au</li>
        <li><span class="contact__key">w:</span> www.kestrelgroup-example.com.au</li>
      </ul>
    </div>
    <div class="card__rule card__rule--bottom"></div>
    <div class="card__band card__band--bottom"></div>
  </section>
</main>
</body>
</html>
```